Design for new 270g product pack

I would like to create packaging design for my 270 g pack of ripe and unripe plantain chips .
I dont want to be too far from the original color scheme and design concept , but I want a new concept.
i.e : I want customers to still be able to connect the old pack design to the new one

The dimension of the standup bag is 17 cm/8cm / 13 cm , I have attached a sketch
I want a window in the packaging , and I would love a curved window , so you can change is but not to a square.
I want an Oval / Curved center .
My Product is Plantain chips , I just used that image as an example
4: The size from the top to the zip is 2.5cm. .

Target Market(s)

Retail

Industry/Entity Type

Food

Colors
EB3D1F
EC4F4E
F09395
F8D3D4
FCEDEE

Requirements
Must have
• similar color scheme with existing pack
Nice to have
• The pack has visible window, and the opaque parts carries the background design of existing pack

```html
<!DOCTYPE html>
<html lang="en">
<head>
<meta charset="utf-8">
<title>Leafora Plantain Chips – 270 gr pouch range</title>
<link rel="stylesheet" href="https://fonts.googleapis.com/css2?family=Luckiest+Guy&family=Oswald:wght@500;600&family=Poppins:wght@400&display=swap">
<style>
  :root {
    --page: #ffffff;
    --pouch: #ededed;
    --pouch-edge: #d8d8d8;
    --pattern-green: #e1eedd;
    --pattern-grey: #e0e0e0;
    --window-top: #7d7069;
    --window-mid: #a59d97;
    --window-low: #d2cecb;
    --oval: #d3d3d3;
    --badge: #b4b70f;
    --badge-ring: #ffffff;
    --title-fill: #ffffff;
    --title-stroke: #1c8f2c;
    --flavour: #ee1a6a;
    --lime: #a9c904;
    --gold: #e3c62a;
    --red: #d7151c;
    --ink: #2b2b2b;
  }
  html, body {
    margin: 0;
    width: 1200px;
    height: 579px;
    overflow: hidden;
    background: var(--page);
  }
  .range { display: block; width: 1200px; height: 579px; }
  .pouch-body { fill: var(--pouch); stroke: var(--pouch-edge); stroke-width: 1; }
  .pattern { fill: var(--pattern); }
  .band { fill: var(--band); }
  .brand-name {
    font-family: "Oswald", sans-serif; font-weight: 600; font-size: 28px;
    fill: var(--brand); text-anchor: middle;
  }
  .web-address {
    font-family: "Poppins", sans-serif; font-size: 7.5px; fill: var(--ink); text-anchor: middle;
  }
  .window-stop-top { stop-color: var(--window-top); }
  .window-stop-mid { stop-color: var(--window-mid); }
  .window-stop-low { stop-color: var(--window-low); }
  .window { opacity: 0.85; }
  .window-sheen { fill: #ffffff; opacity: 0.22; }
  .center-oval { fill: var(--oval); }
  .chip-area { fill: var(--chip); opacity: 0.95; }
  .claim-badge { fill: var(--badge); stroke: var(--badge-ring); stroke-width: 2; }
  .claim-text {
    font-family: "Oswald", sans-serif; font-weight: 500; fill: #ffffff; text-anchor: middle;
  }
  .product-title {
    font-family: "Luckiest Guy", sans-serif; font-size: 23px; fill: var(--title-fill);
    stroke: var(--title-stroke); stroke-width: 4; paint-order: stroke; stroke-linejoin: round;
    text-anchor: middle;
  }
  .flavour-disc { fill: var(--flavour); }
  .weight-badge { fill: var(--badge); stroke: var(--badge-ring); stroke-width: 2; }
  .weight-text {
    font-family: "Oswald", sans-serif; font-weight: 500; fill: #ffffff; text-anchor: middle;
  }
  .lime { --band: var(--lime); --brand: #5f8a00; }
  .gold { --band: var(--gold); --brand: #9a8210; }
  .red  { --band: var(--red);  --brand: #b01016; }
  .green-print { --pattern: var(--pattern-green); }
  .grey-print  { --pattern: var(--pattern-grey); }
  .banana    { --chip: #e6c37a; }
  .pineapple { --chip: #f7df4a; }
  .apple     { --chip: #dcc07a; }
</style>
</head>
<body>
<svg class="range" viewBox="0 0 1200 579" xmlns="http://www.w3.org/2000/svg">
  <defs>
    <linearGradient id="window-tone" x1="0" y1="0" x2="0" y2="1">
      <stop offset="0" class="window-stop-top"/>
      <stop offset="0.55" class="window-stop-mid"/>
      <stop offset="1" class="window-stop-low"/>
    </linearGradient>
    <symbol id="pouch" viewBox="0 0 350 240" width="350" height="240">
      <path class="pouch-body" d="M6,8 Q6,0 16,0 H334 Q344,0 344,8 L348,205 Q300,236 175,232 Q52,236 6,206 Z"/>
      <rect class="pattern" x="7" y="2" width="336" height="56" rx="8" role="img" aria-label="Line drawings of palm trees, pineapples, avocados, apples and bananas"/>
      <text class="brand-name" x="175" y="41">leafora</text>
      <rect class="band" x="0" y="58" width="350" height="15"/>
      <text class="web-address" x="175" y="69">www.leafyacre.farm</text>

      <path class="window" d="M18,74 H332 Q338,74 338,84 L337,150 Q306,140 262,146 Q232,100 175,100 Q118,100 88,146 Q44,140 14,150 L13,84 Q13,74 18,74 Z" fill="url(#window-tone)" role="img" aria-label="Clear curved window showing the chips inside"/>
      <path class="window-sheen" d="M22,78 H90 Q60,110 30,146 L18,148 L17,84 Z"/>
      <path class="window-sheen" d="M328,78 H262 Q292,110 322,144 L334,146 L334,84 Z"/>

      <path class="pattern" d="M10,152 Q46,140 90,148 Q175,186 260,148 Q306,140 342,152 L346,204 Q300,232 175,228 Q54,232 8,205 Z" role="img" aria-label="Fruit line drawing print on lower panel"/>
      <ellipse class="center-oval" cx="175" cy="158" rx="90" ry="56"/>
      <path class="chip-area" d="M112,174 Q118,140 150,146 Q176,132 204,146 Q238,142 238,172 Q232,196 200,192 Q176,204 150,194 Q116,198 112,174 Z" role="img" aria-label="Photo of crisp fruit chips"/>

      <g>
        <circle class="claim-badge" cx="29" cy="98" r="14"/>
        <text class="claim-text" x="29" y="101" font-size="7.5">CRISPY</text>
        <circle class="claim-badge" cx="63" cy="98" r="14"/>
        <text class="claim-text" x="63" y="96" font-size="7">100%</text>
        <text class="claim-text" x="63" y="104" font-size="5">NATURAL</text>
        <circle class="claim-badge" cx="276" cy="99" r="14"/>
        <text class="claim-text" x="276" y="97" font-size="7.5">NO</text>
        <text class="claim-text" x="276" y="106" font-size="7.5">GMO</text>
        <circle class="claim-badge" cx="311" cy="99" r="14"/>
        <text class="claim-text" x="311" y="97" font-size="5">GLUTEN</text>
        <text class="claim-text" x="311" y="106" font-size="8">FREE</text>
      </g>
      <text class="product-title" x="175" y="146">PLANTAIN</text>
      <text class="product-title" x="175" y="169">CHIPS</text>
      <circle class="flavour-disc" cx="276" cy="161" r="24" role="img" aria-label="Flavour icon"/>
      <circle class="weight-badge" cx="172" cy="206" r="14"/>
      <text class="weight-text" x="172" y="206" font-size="11">270</text>
      <text class="weight-text" x="172" y="215" font-size="8">gr</text>
    </symbol>
  </defs>

  <use href="#pouch" class="lime green-print banana"    x="30"  y="37"/>
  <use href="#pouch" class="gold green-print pineapple" x="427" y="38"/>
  <use href="#pouch" class="red green-print apple"      x="816" y="35"/>
  <use href="#pouch" class="lime grey-print banana"     x="34"  y="326"/>
  <use href="#pouch" class="gold grey-print pineapple"  x="431" y="327"/>
  <use href="#pouch" class="red grey-print apple"       x="820" y="324"/>
</svg>
</body>
</html>
```